Wedding Dried Apple Label / Name Place Card

We are looking for a simple but stylish label to be attached via string to a bag of dried apples from my family's fruit farm. The size of the label we think should be similar to the size of a business card. The packaging will be a plastic bag: 4" x 2" x 6".
We would like it to say something like:
Remy & Joss
Est. Sept 10, 2017
Dried Apple Slices
Product of Quenton Fruit Farm
________________
(We need a spot to write in the name of the person and a table number)
Our colors are also grey and navy, and would like these colors to be used.
We have uploaded a photo of the plastic bag.
Wedding

```html
<!DOCTYPE html>
<html lang="en">
<head>
<meta charset="utf-8">
<title>Remy &amp; Joss — Dried Apple Slices Label</title>
<link rel="stylesheet" href="https://fonts.googleapis.com/css2?family=Playfair+Display:wght@400&family=Josefin+Sans:wght@300;400&family=Dancing+Script:wght@700&display=swap">
<style>
  :root {
    --navy: #00007f;
    --grey: #808080;
    --edge: #8c9c9c;
    --white: #ffffff;
    --paper: #ffffff;
  }
  * { box-sizing: border-box; margin: 0; padding: 0; }
  html, body {
    width: 686px;
    height: 1200px;
    overflow: hidden;
    background: var(--paper);
  }
  .tag {
    position: relative;
    width: 686px;
    height: 1200px;
    background: var(--navy);
    border: 3px solid var(--edge);
    border-radius: 38px;
    overflow: hidden;
  }
  .tag__hole {
    position: absolute;
    left: 324px;
    top: 81px;
    width: 38px;
    height: 38px;
    border-radius: 50%;
    background: var(--white);
  }
  .wreath {
    position: absolute;
    left: 88px;
    top: 232px;
    width: 510px;
    height: 505px;
    border-radius: 50%;
    background: radial-gradient(circle at 50% 50%,
      rgba(128,128,128,0) 62%,
      rgba(128,128,128,0.28) 72%,
      rgba(128,128,128,0.28) 86%,
      rgba(128,128,128,0) 98%);
  }
  .couple {
    position: absolute;
    left: 0;
    right: 0;
    top: 340px;
    text-align: center;
    font-family: "Playfair Display", Georgia, serif;
    font-weight: 400;
    color: var(--grey);
    font-size: 96px;
    line-height: 86px;
  }
  .couple__amp { display: block; }
  .guest-line {
    position: absolute;
    top: 805px;
    height: 0;
    border-top: 2px solid var(--grey);
  }
  .guest-line--name { left: 150px; width: 290px; }
  .guest-line--table { left: 466px; width: 70px; }
  .established {
    position: absolute;
    left: 0;
    right: 0;
    top: 850px;
    text-align: center;
    font-family: "Josefin Sans", "Helvetica Neue", sans-serif;
    font-weight: 300;
    font-size: 32px;
    letter-spacing: 1.5px;
    color: var(--white);
  }
  .farm-icon {
    position: absolute;
    left: 295px;
    top: 892px;
    width: 92px;
    height: 104px;
    border-radius: 46px 46px 14px 14px;
    background: radial-gradient(circle at 50% 40%, rgba(128,128,128,0.45), rgba(128,128,128,0.12) 70%);
  }
  .product {
    position: absolute;
    left: 0;
    right: 0;
    top: 1005px;
    text-align: center;
    font-family: "Dancing Script", cursive;
    font-weight: 700;
    font-size: 31px;
    line-height: 40px;
    color: var(--white);
  }
  .origin {
    position: absolute;
    left: 0;
    right: 0;
    top: 1060px;
    text-align: center;
    font-family: "Josefin Sans", "Helvetica Neue", sans-serif;
    font-weight: 400;
    font-size: 29px;
    line-height: 33px;
    color: var(--white);
  }
</style>
</head>
<body>
  <main class="tag">
    <div class="tag__hole"></div>
    <div class="wreath" role="img" aria-label="Hand-drawn grey leafy vine wreath circling the couple's names"></div>
    <h1 class="couple">Remy<span class="couple__amp">&amp;</span>Joss</h1>
    <div class="guest-line guest-line--name" aria-label="Space to write the guest's name"></div>
    <div class="guest-line guest-line--table" aria-label="Space to write the table number"></div>
    <p class="established">EST. SEPT 2017</p>
    <div class="farm-icon" role="img" aria-label="Small grey line illustration of an apple tree"></div>
    <p class="product">Dried Apple Slices</p>
    <p class="origin">Product of Quenton<br>Fruit Farm</p>
  </main>
</body>
</html>
```